Mail - Scan, Sort & Forward - Web Design

We need a web design for a mail scan, store, view and forward service. It is a lifestyle service predicated on freedom, convenience, ease of access, ease of use, security, safety. It involves personal information and is accessed remotely.
No branding or style guide is yet complete so an open pallet is available but design should convey simplicity as it targets demographic 45-75 years travellers but also high net worth multi location professionals, miners and other multi-location workers.
Competitor sites are: (for business description examples)
www.lendrixorbit.example
www.quillobarn.example.au
www.tavenmirefolk.example.au
Updates

Attached files are wireframes which show how the service will work (UI). You should use these to form ideas about your web design for the service. They are not templates nor am I looking for a UI dev (yet).

Target Market(s)

Travellers ( especially retirees) and multi-location workers eg miners

Industry/Entity Type

Business

Requirements
Must have
• Being a lifestyle site, the pages must be low on text, lite layout, imagery addressing the target market.
Navigation should be simple to use
Concept of visitor / member / client should be addressed. The user needs to be able to permission other user groups (read-only)
Talk to reasons why prospects want to use this service.
Nice to have
• access to view nearest Corv Pell office.
Regular call to action like survey, quiz or did you know info which may keep the user returning to the site.
Campaign section which enables customising of campaigns on an ongoing basis
Ability to access and download Terms & conditions, brochures .pdf or other information.
Simulate how service works..video or webcast
Should not have
• Do not want heavy or dense text everywhere. Use imagery where possible. Icons should be thematic not isolated.

```html
<!DOCTYPE html>
<html lang="en">
<head>
<meta charset="utf-8">
<title>Online Mail Service</title>
<link rel="stylesheet" href="https://fonts.googleapis.com/css2?family=Source+Sans+3:wght@400;600;700&display=swap">
<style>
  :root {
    --ink: #555555;
    --ink-soft: #666666;
    --ink-faint: #888888;
    --frame: #d4d4d4;
    --band: #ededed;
    --blue: #0a69ad;
    --blue-dark: #07508a;
    --blue-light: #1a86cc;
    --pale-btn: #e9f3fa;
    --pale-border: #9fc3dc;
    --paper: #ffffff;
  }
  * { box-sizing: border-box; margin: 0; padding: 0; }
  html, body { width: 1167px; height: 1200px; overflow: hidden; background: var(--paper); }
  body { font-family: "Source Sans 3", Arial, sans-serif; color: var(--ink); position: relative; }
  .page { position: absolute; left: 22px; top: 22px; width: 1124px; height: 1150px; border: 1px solid var(--frame); }
  .abs { position: absolute; }

  .flag { left: 643px; top: 45px; width: 30px; height: 23px; background: linear-gradient(135deg, #1f3f8f 0%, #c8283a 50%, #1f3f8f 100%); }
  .lang-select { left: 696px; top: 42px; width: 191px; height: 30px; border: 1px solid #c9c9c9; border-radius: 3px; font-size: 12px; color: var(--ink-faint); padding: 7px 12px; background: #fff; }
  .lang-select::after { content: ""; position: absolute; right: 0; top: 0; width: 28px; height: 28px; border-left: 1px solid #ddd; background: #f4f4f4; }
  .lang-arrow { position: absolute; right: 9px; top: 8px; z-index: 1; }
  .account-btn { top: 44px; height: 26px; border: 1px solid var(--pale-border); border-radius: 3px; background: linear-gradient(#f7fbfe, var(--pale-btn)); font-size: 12px; color: #2c5f86; text-align: center; line-height: 24px; }
  .login { left: 917px; width: 63px; }
  .signup { left: 992px; width: 64px; }

  .brand { left: 147px; top: 108px; font-size: 56px; font-weight: 700; color: var(--ink); letter-spacing: -1px; line-height: 1; }
  .tagline { left: 150px; top: 172px; font-size: 16px; color: var(--ink-soft); }

  .main-nav { left: 502px; top: 138px; height: 37px; display: flex; gap: 6px; }
  .nav-item { height: 37px; background: linear-gradient(var(--blue-light), var(--blue) 55%, var(--blue-dark)); color: #fff; font-weight: 700; font-size: 16px; line-height: 37px; text-align: center; }
  .nav-rule { left: 485px; top: 182px; width: 660px; height: 1px; background: #e6e6e6; }

  .hero-photo { left: 157px; top: 246px; width: 375px; height: 368px; background: radial-gradient(ellipse at 50% 40%, #d9d4cf 0%, #bdb7b2 55%, #ececec 100%); }
  .hero-title { left: 602px; top: 296px; font-size: 46px; font-weight: 600; color: var(--ink); letter-spacing: -0.5px; line-height: 1; }
  .hero-sub { left: 603px; top: 348px; font-size: 24px; color: var(--ink); line-height: 1; }
  .hero-copy { left: 603px; top: 402px; width: 470px; font-size: 15px; line-height: 27.5px; color: var(--ink); letter-spacing: 0.3px; }
  .btn-blue { background: linear-gradient(var(--blue-light), var(--blue) 55%, var(--blue-dark)); color: #fff; font-weight: 700; font-size: 14px; text-align: center; border-radius: 2px; }
  .hero-btn { left: 601px; top: 519px; width: 147px; height: 34px; line-height: 34px; }

  .benefits { left: 23px; top: 614px; width: 1122px; height: 90px; background: var(--band); border-top: 1px solid #dedede; border-bottom: 1px solid #dedede; }
  .benefit { position: absolute; top: 26px; }
  .benefit h3 { font-size: 15px; font-weight: 600; color: #333; line-height: 1.2; }
  .benefit p { font-size: 12.5px; color: var(--ink-soft); margin-top: 3px; }

  .intro-title { left: 126px; top: 750px; font-size: 26px; color: var(--ink); line-height: 1; }
  .intro-copy { left: 126px; top: 788px; width: 490px; font-size: 15px; line-height: 26px; color: var(--ink); }
  .intro-copy p + p { margin-top: 10px; }
  .intro-btn { left: 472px; top: 1009px; width: 130px; height: 35px; line-height: 35px; }

  .social { top: 1074px; width: 28px; height: 28px; border-radius: 50%; background: radial-gradient(circle at 40% 35%, #ffffff, #dcdcdc); border: 1px solid #cfcfcf; }

  .quick-link { left: 719px; width: 338px; height: 40px; border: 1px solid #d6d6d6; border-radius: 2px; background: linear-gradient(#ffffff, #f1f1f1); font-size: 16.5px; color: var(--ink); line-height: 38px; padding-left: 30px; }
  .quick-link svg { position: absolute; left: 13px; top: 14px; }

  .promo { left: 721px; top: 931px; width: 337px; height: 175px; background: linear-gradient(var(--blue-light), var(--blue) 60%, var(--blue-dark)); color: #fff; text-align: center; }
  .promo-lead { position: absolute; top: 24px; width: 100%; font-size: 21px; font-weight: 700; letter-spacing: -0.3px; }
  .promo-big { position: absolute; top: 50px; width: 100%; font-size: 56px; font-weight: 700; line-height: 1; }
  .promo-btn { position: absolute; left: 80px; top: 117px; width: 175px; height: 36px; background: linear-gradient(#ffffff, #dadada); color: #555; font-weight: 700; font-size: 17px; line-height: 36px; }

  .footer-nav, .legal { top: 1137px; font-size: 13.5px; color: var(--ink-faint); word-spacing: 1px; }
  .footer-nav { left: 126px; }
  .legal { left: 723px; }
  .sep { margin: 0 9px; }
</style>
</head>
<body>
  <div class="page"></div>

  <div class="abs flag" role="img" aria-label="Flag for the current language"></div>
  <div class="abs lang-select">Choose Language...
    <svg class="lang-arrow" width="8" height="12" viewBox="0 0 8 12"><path d="M1 4 L4 1 L7 4 M1 8 L4 11 L7 8" fill="none" stroke="#888" stroke-width="1.2"/></svg>
  </div>
  <div class="abs account-btn login">Login</div>
  <div class="abs account-btn signup">Sign Up</div>

  <div class="abs brand">Your Logo</div>
  <div class="abs tagline">Keeping you intouch when your on the go!</div>

  <nav class="abs main-nav">
    <div class="nav-item" style="width:43px">
      <svg width="18" height="16" viewBox="0 0 18 16" style="margin-top:10px"><path d="M9 1 L17 8 H14.5 V15 H10.5 V10.5 H7.5 V15 H3.5 V8 H1 Z" fill="#fff"/></svg>
    </div>
    <div class="nav-item" style="width:104px">About Us</div>
    <div class="nav-item" style="width:116px">How it works</div>
    <div class="nav-item" style="width:102px">Pricing</div>
    <div class="nav-item" style="width:51px">FAQs</div>
    <div class="nav-item" style="width:102px">Contact Us</div>
  </nav>
  <div class="abs nav-rule"></div>

  <div class="abs hero-photo" role="img" aria-label="Photo of a smiling couple holding a globe sign and a mail sign"></div>
  <h1 class="abs hero-title">Online Mail Service</h1>
  <div class="abs hero-sub">never get tied down by your mailbox again</div>
  <div class="abs hero-copy">Get your mail and stay intouch, even if you travel or live overseas. Why wait? Get your important mail scanned and read it online within a day! So stay intouch when you plan on being away!</div>
  <div class="abs btn-blue hero-btn">Find Out More</div>

  <section class="abs benefits">
    <div class="benefit" style="left:107px"><h3>Ease of use</h3><p>Mail, scan, sort &amp; forward</p></div>
    <div class="benefit" style="left:309px"><h3>Ease of access</h3><p>Online mail access 24/7</p></div>
    <div class="benefit" style="left:501px"><h3>Freedom</h3><p>Live &amp; travel anywhere</p></div>
    <div class="benefit" style="left:688px"><h3>Piece of mind</h3><p>Protect your identity</p></div>
    <div class="benefit" style="left:870px"><h3>Security</h3><p style="margin-top:5px">Securely store your mail</p></div>
  </section>

  <h2 class="abs intro-title">ONLINE MAIL SERVICE</h2>
  <div class="abs intro-copy">
    <p>A platform built to be simple convenient and reliable, with high security, 24/7 online mail access, you can have piece of mind you will be able to get your mail where ever and when ever!</p>
    <p>Our online mail service couldn't be easier! Get your documents scanned and read online with in a day, and be able to keep on top and manage your mail all by the click of a finger! View our video to find out more about our process!</p>
  </div>
  <div class="abs btn-blue intro-btn">Find Out More</div>

  <div class="abs social" style="left:132px"></div>
  <div class="abs social" style="left:172px"></div>
  <div class="abs social" style="left:212px"></div>

  <div class="abs quick-link" style="top:751px"><svg width="7" height="11" viewBox="0 0 7 11"><path d="M1 1 L5.5 5.5 L1 10" fill="none" stroke="#0a69ad" stroke-width="2"/></svg>WATCH OUR VIDEO TO GET STARTED</div>
  <div class="abs quick-link" style="top:809px"><svg width="7" height="11" viewBox="0 0 7 11"><path d="M1 1 L5.5 5.5 L1 10" fill="none" stroke="#0a69ad" stroke-width="2"/></svg>FIND THE NEAREST CORV PELL OFFICE</div>
  <div class="abs quick-link" style="top:867px"><svg width="7" height="11" viewBox="0 0 7 11"><path d="M1 1 L5.5 5.5 L1 10" fill="none" stroke="#0a69ad" stroke-width="2"/></svg>JUST FOR FUN, QUESTIONNAIRE!</div>

  <aside class="abs promo">
    <div class="promo-lead">SIGN UP THIS MONTH AND GET</div>
    <div class="promo-big">HALF PRICE</div>
    <div class="promo-btn">SIGN UP NOW!</div>
  </aside>

  <div class="abs footer-nav">About Us<span class="sep">|</span>Tour<span class="sep">|</span>How It Works<span class="sep">|</span>Pricing<span class="sep">|</span>FAQs<span class="sep">|</span>Contact</div>
  <div class="abs legal">Terms &amp; Conditions<span class="sep">|</span>Privacy<span class="sep">|</span>© 2011 Your Logo</div>
</body>
</html>
```